Medical Practice Business Card

we need a business card for our new medical ophthalmology practice based in Needham Massachusetts. we are looking for a simple , modern and elegant design.
the card needs to contain the following
1- the logo of our practice (please see attached file)
2- the name of the practice : "Silver Birch Retina Care"
3- Doctor's Name: Tobias Rendell MD PhD
4- Specialty: Board-Certified Vitreoretinal Surgeon
5- practice address: 87 Larkspur Ave, Suite 210, Needham MA 02481
7- Office number: 617- 482 - 7730
8- fax number: 617- 391 - 2268
9- email: info@sbretinahub.example
10- website: www.sbretinahub.example

```html
<!DOCTYPE html>
<html lang="en">
<head>
<meta charset="utf-8">
<title>Silver Birch Retina Care – Business Card</title>
<link rel="stylesheet" href="https://fonts.googleapis.com/css2?family=Cinzel:wght@700&family=Arimo:wght@400&display=swap">
<style>
  :root {
    --page: #e8e8e8;
    --navy: #1b3a63;
    --navy-raised: #2a5383;
    --accent-blue: #3d82d8;
    --band-cyan: #7cdcea;
    --band-blue: #1666c6;
    --white: #ffffff;
    --rule: #5f7ea3;
  }
  * { margin: 0; padding: 0; box-sizing: border-box; }
  html, body {
    width: 1200px; height: 802px; overflow: hidden;
    background: var(--page);
  }
  .sheet {
    width: 1200px; height: 802px;
    display: flex; align-items: center; justify-content: center; gap: 40px;
  }
  .card {
    position: relative;
    width: 540px; height: 309px;
    background: var(--navy);
    overflow: hidden;
    box-shadow: 0 6px 18px rgba(0,0,0,.18);
  }
  .card svg.wave { position: absolute; inset: 0; }

  .practice-name {
    position: absolute; left: 34px; top: 116px; width: 216px;
    font-family: "Arimo", sans-serif; font-weight: 400;
    color: var(--white); font-size: 17px; line-height: 1.2;
    white-space: nowrap;
  }
  .divider {
    position: absolute; left: 262px; top: 60px;
    width: 1px; height: 130px; background: var(--rule);
  }
  .doctor {
    position: absolute; left: 282px; top: 51px;
    font-family: "Cinzel", serif; font-weight: 700;
    color: var(--accent-blue); font-size: 15px;
  }
  .specialty {
    position: absolute; left: 282px; top: 72px;
    font-family: "Arimo", sans-serif; color: var(--white); font-size: 11.5px;
  }
  .contacts {
    position: absolute; left: 282px; top: 98px; list-style: none;
    font-family: "Arimo", sans-serif; color: var(--white); font-size: 11.5px;
  }
  .contacts li { display: flex; align-items: center; gap: 7px; height: 16px; }
  .contacts svg { width: 10px; height: 10px; flex: none; }
  .address {
    position: absolute; right: 22px; bottom: 24px; text-align: right;
    font-family: "Arimo", sans-serif; color: var(--white); font-size: 12.5px; line-height: 1.45;
  }

  .card-back { display: flex; align-items: center; justify-content: center; }
  .back-name {
    font-family: "Arimo", sans-serif; font-weight: 400;
    color: var(--navy-raised); font-size: 28px; white-space: nowrap;
  }
</style>
</head>
<body>
<main class="sheet">
  <section class="card card-front">
    <svg class="wave" width="540" height="309" viewBox="0 0 540 309">
      <defs>
        <linearGradient id="bandGradient" x1="0" y1="1" x2="1" y2="0">
          <stop offset="0" stop-color="var(--band-cyan)"/>
          <stop offset="1" stop-color="var(--band-blue)"/>
        </linearGradient>
      </defs>
      <path d="M0,255 C200,252 358,240 424,175 C466,133 488,58 540,38 L540,309 L0,309 Z" fill="var(--white)"/>
      <path d="M0,265 C200,262 360,250 430,185 C470,145 492,70 540,50 L540,309 L0,309 Z" fill="url(#bandGradient)"/>
    </svg>

    <p class="practice-name">Silver Birch Retina Care</p>
    <div class="divider"></div>

    <h1 class="doctor">TOBIAS RENDELL MD PHD</h1>
    <p class="specialty">Board-Certified Vitreoretinal Surgeon</p>
    <ul class="contacts">
      <li><svg viewBox="0 0 10 10"><path d="M2 1l2 2-1 1.2c.6 1.2 1.5 2.1 2.8 2.8L7 6l2 2-1.3 1.3C4.5 9 1 5.5.7 2.3z" fill="var(--white)"/></svg>617- 482 - 7730</li>
      <li><svg viewBox="0 0 10 10"><rect x="2.5" y="1" width="5" height="3" fill="none" stroke="var(--white)"/><rect x="1" y="4" width="8" height="4" rx="1" fill="var(--white)"/></svg>617- 391 - 2268</li>
      <li><svg viewBox="0 0 10 10"><rect x="1" y="2" width="8" height="6" fill="none" stroke="var(--white)"/><path d="M1 2l4 3.5L9 2" fill="none" stroke="var(--white)"/></svg>info@sbretinahub.example</li>
      <li><svg viewBox="0 0 10 10"><circle cx="5" cy="5" r="4" fill="none" stroke="var(--white)"/><path d="M1 5h8M5 1c-2 2.5-2 5.5 0 8M5 1c2 2.5 2 5.5 0 8" fill="none" stroke="var(--white)" stroke-width=".7"/></svg>www.sbretinahub.example</li>
    </ul>

    <p class="address">87 Larkspur Ave, Suite 210<br>Needham MA 02481</p>
  </section>

  <section class="card card-back">
    <p class="back-name">Silver Birch Retina Care</p>
  </section>
</main>
</body>
</html>
```